Company or website name

Heron Gate

Slogan or Tagline

Artisan toothpaste

Describe your company and organization and target audience

The name itself should look like it was a brand that was created in 1880, but someone recently re-created, or re-branded it. In other words it should feel like it has a heritage, without looking old or tired. The additional writing on the label s

The design should have the following

needs to fit on tube

This design should not have this in the entries

35+ affluent

Colors to use in the design

http://www.stashbox-files.example/upload.php

Briefly describe your contest

Artisan Toothpaste

```html
<!DOCTYPE html>
<html lang="en">
<head>
<meta charset="utf-8">
<title>Heron Gate – Artisan Toothpaste Label</title>
<link rel="stylesheet" href="https://fonts.googleapis.com/css2?family=UnifrakturMaguntia&family=Pinyon+Script&family=Kalam:wght@400&display=swap">
<style>
  :root {
    --page: #ffffff;
    --paper-light: #f4f0e4;
    --paper-mid: #e6e0cf;
    --paper-edge: #b9b3a3;
    --ink: #161616;
    --ink-soft: #2e2b27;
    --ornament: #9a6d6d;
    --ornament-light: #d9c3bd;
    --rule: #7a5a58;
  }
  * { margin: 0; padding: 0; box-sizing: border-box; }
  html, body { width: 1200px; height: 720px; overflow: hidden; background: var(--page); }
  .label {
    position: relative;
    width: 1200px;
    height: 720px;
    overflow: hidden;
    background:
      radial-gradient(ellipse 70% 65% at 50% 48%, var(--paper-light) 0%, var(--paper-light) 45%, var(--paper-mid) 78%, var(--paper-edge) 100%);
    box-shadow: inset 0 0 0 14px var(--page), inset 0 0 60px 30px rgba(120,112,96,0.35);
    color: var(--ink);
  }
  .brand-name {
    position: absolute;
    top: 92px; left: 0; width: 100%;
    text-align: center;
    font-family: "UnifrakturMaguntia", serif;
    font-size: 150px;
    line-height: 1;
    color: var(--ink);
    letter-spacing: 2px;
  }
  .maker-line {
    position: absolute;
    left: 0; width: 100%;
    text-align: center;
    font-family: "Pinyon Script", cursive;
    font-size: 36px;
    line-height: 1;
    color: var(--ink-soft);
  }
  .maker-line--crafted { top: 286px; }
  .maker-line--limited { top: 328px; }
  .product-name {
    position: absolute;
    top: 372px; left: 0; width: 100%;
    text-align: center;
    font-family: "UnifrakturMaguntia", serif;
    font-size: 50px;
    line-height: 1;
    color: var(--ink);
  }
  .ornament {
    position: absolute;
    top: 276px;
    width: 144px;
    height: 224px;
  }
  .ornament--left { left: 211px; }
  .ornament--right { left: 864px; }
  .base-line {
    position: absolute;
    top: 490px; left: 0; width: 100%;
    display: flex;
    justify-content: center;
    align-items: center;
    gap: 26px;
  }
  .base-line__text {
    font-family: "Pinyon Script", cursive;
    font-size: 34px;
    line-height: 1;
    color: var(--ink-soft);
  }
  .base-line__rule { width: 92px; height: 14px; }
  .batch-details {
    position: absolute;
    top: 592px; left: 0; width: 100%;
    height: 60px;
    font-size: 34px;
    line-height: 1;
  }
  .batch-details__label {
    position: absolute;
    font-family: "Pinyon Script", cursive;
    color: var(--ink-soft);
  }
  .batch-details__value {
    position: absolute;
    top: 4px;
    font-family: "Kalam", cursive;
    font-size: 28px;
    color: var(--ink);
  }
</style>
</head>
<body>
<main class="label">
  <h1 class="brand-name">Heron Gate</h1>

  <p class="maker-line maker-line--crafted">Created by American Craftsmen</p>
  <p class="maker-line maker-line--limited">In limited quantities</p>

  <svg class="ornament ornament--left" viewBox="0 0 144 224" role="img" aria-label="Ornate candelabra-style flourish ornament">
    <defs>
      <linearGradient id="ornamentFillLeft" x1="0" y1="0" x2="0" y2="1">
        <stop offset="0" stop-color="var(--ornament)" stop-opacity="0.55"/>
        <stop offset="1" stop-color="var(--ornament-light)" stop-opacity="0.35"/>
      </linearGradient>
    </defs>
    <rect x="0" y="0" width="144" height="224" rx="18" fill="url(#ornamentFillLeft)"/>
  </svg>

  <svg class="ornament ornament--right" viewBox="0 0 144 224" role="img" aria-label="Ornate candelabra-style flourish ornament">
    <defs>
      <linearGradient id="ornamentFillRight" x1="0" y1="0" x2="0" y2="1">
        <stop offset="0" stop-color="var(--ornament)" stop-opacity="0.55"/>
        <stop offset="1" stop-color="var(--ornament-light)" stop-opacity="0.35"/>
      </linearGradient>
    </defs>
    <rect x="0" y="0" width="144" height="224" rx="18" fill="url(#ornamentFillRight)"/>
  </svg>

  <h2 class="product-name">Artisan Toothpaste</h2>

  <div class="base-line">
    <svg class="base-line__rule" viewBox="0 0 92 14" aria-hidden="true">
      <line x1="2" y1="7" x2="90" y2="7" stroke="var(--rule)" stroke-width="2"/>
      <circle cx="46" cy="7" r="4" fill="var(--rule)"/>
    </svg>
    <span class="base-line__text">Chardonnay Base</span>
    <svg class="base-line__rule" viewBox="0 0 92 14" aria-hidden="true">
      <line x1="2" y1="7" x2="90" y2="7" stroke="var(--rule)" stroke-width="2"/>
      <circle cx="46" cy="7" r="4" fill="var(--rule)"/>
    </svg>
  </div>

  <div class="batch-details">
    <span class="batch-details__label" style="left:101px;">Harvest Date:</span>
    <span class="batch-details__value" style="left:307px;">2008/10</span>
    <span class="batch-details__label" style="left:509px;">Created On:</span>
    <span class="batch-details__value" style="left:696px;">2008/11</span>
    <span class="batch-details__label" style="left:888px;">No.:</span>
    <span class="batch-details__value" style="left:967px;">112/344</span>
  </div>
</main>
</body>
</html>
```